依頼詳細
・リスティングでの運用を考えているので、コンバージョンを期待できるデザイン、サイト構成
・レスポンシブでコーディングするためそれを念頭に置いたデザイン
・提案デザインはスマホ、PC両画面でお願いします。
・サイト構成も変わる可能性が高いので、HTMLやCSSでの変更が容易なデザイン
(メニューなどを画像にしないetc)
・奇抜さよりも安心感
・病院関係のウェブサイト構築実績のある方歓迎
・病院の場所はみなとみらいです。
ページ数
2ページ
希望イメージ
シンプル 複雑
単色 カラフル
暗い 明るい
日常 高級
遊び心 厳粛
未来的 伝統的
女性的 男性的
希望する色
青系、水色系、緑系、黄・オレンジ系
納品ファイル
• 高解像度JPG (.jpg)
• フォトショップ形式 (.psd)
補足説明
■ 補足
--------------------------------
・基本HTMLコーディングは無しで構いませんが、
対応可能な方はコーディング作業についてもお見積ください。

・採用された方は今後も引続き作業をお願いすることになると思います。

■ 注意点

・お渡しできる素材は、サイトマップのみとなります
・病院名なども決まっていないので、ロゴなどは仮のもので構いません。
・サイトの中の文言なども仮の文章で構いません。
・写真素材も仮のもので構いません。
(最終的には素材もしくは撮影した写真に入れ替えます。)

○想定サイトマップ
診療科目
病院案内
├ ご挨拶・理念
├ 施設案内
└ ドクター紹介
アクセス
よくある質問
採用情報
サイトマップ
お問い合わせ
予約

※サイト構成も決定ではないので提案頂く形でも構いません。

参考サイト
http://www.hizuki-dental.com/
https://www.clinic-kotobe.com/
ウェブサイトの構成が、内科・整形外科・歯科の診療科目を一つのサイトで集患する形に変更になりました。大きい枠組みで変わるのはこれ以降はないと思います。素敵なデザイナー様との出会いを期待しております。
お盆に入ってしまうので、締切を延長させていただきました。今後も数々の案件抱えておりますので、長いお付き合いができるデザイナー様との出会いを期待しております。
たくさんのご応募、誠にありがとうございます!

これから社内で選定を行います。
一週間以内には決定できると思いますので少々お待ち頂ければと思います。
よろしくお願いいたします。
デザインの選定に時間がかかっておりますので、決定までもう少々お待ち頂ければと思います。申し訳ありません、よろしくお願いいたします。
■ 選んだ理由

シンプルにデザインがまとまっていたところと、アイコンなどを使いぱっと見た時のわかりやすさ、写真を変更しても違和感なくマッチしそうな点などを評価させていただきました。

■ 提案者全員のお礼・コメント

この度は弊社コンペにご参加頂き誠にありがとうございます。
優れたデザイン・提案を多数頂きとても感謝しております。

ギリギリまでどの提案を採用させていただくか迷いましたが、
今回はこのような結果となりました。

またの機会がありましたら、またぜひご参加頂ければ幸いです。
ありがとうございました。

```html
<!DOCTYPE html>
<html lang="ja">
<head>
<meta charset="utf-8">
<title>ソラノクリニック</title>
<link href="https://fonts.googleapis.com/css2?family=Noto+Sans+JP:wght@400;500;700&display=swap" rel="stylesheet">
<style>
:root{
  --teal:#1fb6c4;
  --teal-dark:#14909c;
  --teal-soft:#e4f6f8;
  --pink:#e8508a;
  --ink:#444;
  --muted:#888;
  --line:#d9e6e8;
  --paper:#ffffff;
  --grey:#f4f6f6;
}
*{box-sizing:border-box;margin:0;padding:0}
html,body{width:766px;height:1200px;overflow:hidden;background:var(--paper)}
body{font-family:"Noto Sans JP",sans-serif;color:var(--ink);font-size:8px;line-height:1.5}
.page{width:766px;height:1200px;position:relative;overflow:hidden}
.wrap{width:410px;margin:0 auto;position:relative}

.site-header{height:26px;display:flex;align-items:center;justify-content:space-between;padding:0 18px 0 22px}
.brand{display:flex;align-items:center;gap:5px;font-weight:700;color:var(--teal);font-size:12px;white-space:nowrap}
.brand-dot{width:11px;height:11px;border-radius:50%;background:var(--teal);flex:none}
.header-tel{display:flex;align-items:center;gap:4px;color:var(--teal-dark);font-weight:700;font-size:11px}
.header-tel small{display:block;font-size:5px;font-weight:400;color:var(--muted)}
.tel-icon{width:12px;height:12px;background:var(--teal);border-radius:2px;display:flex;align-items:center;justify-content:center}

.hero{height:166px;position:relative;display:flex}
.hero-photo{height:100%}
.hero-left{width:185px;background:linear-gradient(135deg,#cfe3e6,#f1ece6 60%,#9fc8cf)}
.hero-center{flex:1;background:linear-gradient(180deg,#f6f1ea,#e9e3d8);position:relative}
.hero-right{width:176px;background:linear-gradient(160deg,#bfe0ea,#dfeee0 55%,#a9cfa6)}
.hero-copy{position:absolute;left:24px;top:20px}
.hero-copy span{display:inline-block;padding:2px 6px;margin-bottom:4px;font-size:12px;font-weight:700;color:#fff}
.hero-copy .c1{background:var(--teal)}
.hero-copy .c2{background:var(--pink)}

.global-nav{height:38px;border-bottom:1px solid var(--line)}
.global-nav ul{list-style:none;display:flex;justify-content:space-between;width:380px;margin:0 auto;height:100%}
.global-nav li{flex:1;display:flex;flex-direction:column;align-items:center;justify-content:center;gap:2px;font-size:7px;color:var(--teal-dark);border-right:1px dotted var(--line)}
.global-nav li:last-child{border-right:0}
.nav-icon{width:12px;height:12px}

.section-title{text-align:center;color:var(--teal);font-size:10px;font-weight:500}
.section-title small{display:block;font-size:5px;color:var(--muted);letter-spacing:.1em}

.about{height:160px;padding-top:18px}
.about-body{display:flex;gap:18px;margin-top:14px}
.doctor-photo{width:140px;height:100px;flex:none;background:linear-gradient(135deg,#e8eef0,#cfdde2 60%,#f3f3f3)}
.about-text{flex:1}
.about-text h3{color:var(--teal);font-size:8px;font-weight:700;line-height:1.4;margin:4px 0 6px}
.about-text p{font-size:6px;color:var(--muted);line-height:1.6}
.btn{display:inline-block;margin-top:8px;border:1px solid var(--teal);color:var(--teal);font-size:6px;padding:2px 12px;border-radius:2px;background:#fff}
.about-text .btn{margin-left:80px}

.services{height:273px;background:var(--grey);padding-top:15px}
.services-lead{font-size:6px;color:var(--muted);margin:10px 0 8px 10px}
.service{display:flex;gap:16px;margin-bottom:12px}
.service-photo{width:123px;height:84px;flex:none}
.service-1 .service-photo{background:linear-gradient(135deg,#f1ece4,#d8e4e8 55%,#b9ccd2)}
.service-2 .service-photo{background:linear-gradient(135deg,#e5ece6,#c7d8d8 50%,#eef1f0)}
.service h4{font-size:10px;color:var(--teal);font-weight:700;margin-top:6px;display:flex;align-items:center;gap:4px}
.service h4::before{content:"";width:8px;height:8px;background:var(--teal);border-radius:50%}
.service p{font-size:6px;color:var(--muted);line-height:1.6;margin-top:3px}
.service .btn{margin-top:3px}

.news{height:102px;background:var(--teal);color:#fff;padding-top:14px}
.news .section-title{color:#fff}
.news .section-title small{color:#dff}
.news-list{list-style:none;margin:8px auto 0;width:230px}
.news-list li{font-size:6px;display:flex;gap:8px;border-bottom:1px dotted rgba(255,255,255,.5);padding:1px 0}

.overview{height:175px;padding-top:18px}
.overview-body{display:flex;gap:18px;margin-top:10px}
.overview-info{width:130px;flex:none}
.overview-info .brand{font-size:11px}
.overview-tel{font-size:11px;color:var(--teal-dark);font-weight:700;margin:2px 0}
.overview-address{font-size:5px;color:var(--muted)}
.building-photo{width:115px;height:62px;margin-top:4px;background:linear-gradient(180deg,#b9d6ea,#d9e2e6 55%,#9aa8a8)}
.hours-box{flex:1;margin-top:18px}
.hours{width:100%;border-collapse:collapse;font-size:6px}
.hours th{background:var(--teal);color:#fff;font-weight:500;padding:3px 2px}
.hours td{border:1px solid var(--line);text-align:center;padding:5px 2px;color:var(--teal-dark)}
.hours td:first-child{font-size:5px;color:var(--ink);white-space:nowrap}
.hours-note{font-size:5px;color:var(--muted);margin-top:3px}

.map{height:180px;background:linear-gradient(135deg,#e8e6df,#efece4 45%,#b9d7e6 70%,#a8cde0)}

.site-footer{height:80px;background:#f2f6f6;position:relative}
.footer-links{display:flex;justify-content:center;gap:34px;padding-top:10px}
.footer-links ul{list-style:none;font-size:5.5px;color:var(--muted);line-height:1.9}
.copyright{position:absolute;bottom:0;left:0;right:0;height:12px;background:var(--teal);color:#fff;font-size:5px;text-align:center;line-height:12px}
</style>
</head>
<body>
<div class="page">
  <header class="site-header">
    <div class="brand"><span class="brand-dot"></span>ソラノクリニック</div>
    <div class="header-tel">
      <span class="tel-icon"><svg width="8" height="8" viewBox="0 0 24 24"><path fill="#fff" d="M6.6 10.8a15 15 0 0 0 6.6 6.6l2.2-2.2c.3-.3.7-.4 1-.2 1.1.4 2.3.6 3.6.6.6 0 1 .4 1 1V20c0 .6-.4 1-1 1A17 17 0 0 1 3 4c0-.6.4-1 1-1h3.5c.6 0 1 .4 1 1 0 1.3.2 2.5.6 3.6.1.3 0 .7-.2 1z"/></svg></span>
      <div><small>ご予約・お問い合わせ</small>0120-98-7654</div>
    </div>
  </header>

  <section class="hero">
    <div class="hero-photo hero-left" role="img" aria-label="医師と患者が笑顔で話す写真"></div>
    <div class="hero-photo hero-center" role="img" aria-label="明るい待合室の写真">
      <div class="hero-copy">
        <span class="c1">ソラノクリニックは</span><br>
        <span class="c2">みなとみらいの身近な医院です</span>
      </div>
    </div>
    <div class="hero-photo hero-right" role="img" aria-label="車椅子の患者と家族の写真"></div>
  </section>

  <nav class="global-nav">
    <ul>
      <li><svg class="nav-icon" viewBox="0 0 24 24"><rect x="4" y="3" width="16" height="18" rx="2" fill="none" stroke="#1fb6c4" stroke-width="2"/><path d="M8 9h8M8 13h8M8 17h5" stroke="#1fb6c4" stroke-width="2"/></svg>診療科目</li>
      <li><svg class="nav-icon" viewBox="0 0 24 24"><path d="M3 21V9l9-6 9 6v12z" fill="none" stroke="#1fb6c4" stroke-width="2"/><path d="M12 10v6M9 13h6" stroke="#1fb6c4" stroke-width="2"/></svg>病院案内</li>
      <li><svg class="nav-icon" viewBox="0 0 24 24"><circle cx="12" cy="8" r="4" fill="none" stroke="#1fb6c4" stroke-width="2"/><path d="M4 21c1-5 15-5 16 0" fill="none" stroke="#1fb6c4" stroke-width="2"/></svg>ドクター紹介</li>
      <li><svg class="nav-icon" viewBox="0 0 24 24"><path d="M12 22s7-7 7-12a7 7 0 0 0-14 0c0 5 7 12 7 12z" fill="none" stroke="#1fb6c4" stroke-width="2"/><circle cx="12" cy="10" r="2.5" fill="#1fb6c4"/></svg>アクセス</li>
      <li><svg class="nav-icon" viewBox="0 0 24 24"><circle cx="12" cy="12" r="9" fill="none" stroke="#1fb6c4" stroke-width="2"/><path d="M9.5 9.5a2.5 2.5 0 1 1 3.5 2.3c-.7.3-1 .8-1 1.5M12 17v.5" fill="none" stroke="#1fb6c4" stroke-width="2"/></svg>よくある質問</li>
      <li><svg class="nav-icon" viewBox="0 0 24 24"><rect x="3" y="7" width="18" height="13" rx="2" fill="none" stroke="#1fb6c4" stroke-width="2"/><path d="M9 7V4h6v3" fill="none" stroke="#1fb6c4" stroke-width="2"/></svg>採用情報</li>
    </ul>
  </nav>

  <section class="about">
    <div class="wrap">
      <h2 class="section-title">ソラノクリニックについて<small>ABOUT US</small></h2>
      <div class="about-body">
        <div class="doctor-photo" role="img" aria-label="院長の写真"></div>
        <div class="about-text">
          <h3>地域の皆さまに寄り添う<br>安心の医療をめざします</h3>
          <p>当院は内科・整形外科・歯科をそなえた地域のクリニックです。<br>どんな小さなお悩みでも気軽にご相談ください。<br>丁寧な説明とわかりやすい診療を心がけています。<br>スタッフ一同、皆さまのご来院をお待ちしております。</p>
          <a class="btn">ご挨拶・理念</a>
        </div>
      </div>
    </div>
  </section>

  <section class="services">
    <div class="wrap">
      <h2 class="section-title">診療案内<small>MEDICAL</small></h2>
      <p class="services-lead">当院では以下の診療科目を受け付けております。</p>
      <div class="service service-1">
        <div class="service-photo" role="img" aria-label="内科の診察風景の写真"></div>
        <div>
          <h4>内科</h4>
          <p>風邪や発熱から生活習慣病まで幅広く診療します。</p>
          <a class="btn">詳しく見る</a>
        </div>
      </div>
      <div class="service service-2">
        <div class="service-photo" role="img" aria-label="整形外科のリハビリ室の写真"></div>
        <div>
          <h4>整形外科</h4>
          <p>腰や膝の痛み、けがの治療とリハビリを行います。</p>
          <a class="btn">詳しく見る</a>
        </div>
      </div>
    </div>
  </section>

  <section class="news">
    <h2 class="section-title">新着情報<small>NEWS</small></h2>
    <ul class="news-list">
      <li><span>2024.08.10</span>夏季休診日のお知らせ</li>
      <li><span>2024.07.25</span>インフルエンザ予防接種について</li>
      <li><span>2024.07.01</span>診療時間変更のお知らせ</li>
      <li><span>2024.06.15</span>ホームページを開設しました</li>
    </ul>
  </section>

  <section class="overview">
    <div class="wrap">
      <h2 class="section-title">医院概要<small>OUTLINE</small></h2>
      <div class="overview-body">
        <div class="overview-info">
          <div class="brand"><span class="brand-dot"></span>ソラノクリニック</div>
          <div class="overview-tel">0120-98-7654</div>
          <p class="overview-address">横浜市西区みなとみらい0-0-0 ソラノビル2F</p>
          <div class="building-photo" role="img" aria-label="クリニックが入る建物の写真"></div>
        </div>
        <div class="hours-box">
          <table class="hours">
            <tr><th>診療時間</th><th>月</th><th>火</th><th>水</th><th>木</th><th>金</th><th>土</th><th>日</th></tr>
            <tr><td>9:00〜12:30</td><td>○</td><td>○</td><td>○</td><td>○</td><td>○</td><td>○</td><td>ー</td></tr>
            <tr><td>14:30〜18:30</td><td>○</td><td>○</td><td>ー</td><td>○</td><td>○</td><td>ー</td><td>ー</td></tr>
          </table>
          <p class="hours-note">休診日：水曜午後・土曜午後・日曜・祝日</p>
        </div>
      </div>
    </div>
  </section>

  <div class="map" role="img" aria-label="みなとみらい周辺の地図"></div>

  <footer class="site-footer">
    <div class="footer-links">
      <ul><li>トップ</li><li>診療科目</li><li>内科</li></ul>
      <ul><li>病院案内</li><li>ご挨拶・理念</li><li>施設案内</li></ul>
      <ul><li>ドクター紹介</li><li>アクセス</li><li>よくある質問</li></ul>
      <ul><li>採用情報</li><li>お問い合わせ</li><li>予約</li></ul>
    </div>
    <div class="copyright">Copyright © ソラノクリニック All Rights Reserved.</div>
  </footer>
</div>
</body>
</html>
```